BHAG Poster

We like creativity and visual boxes and shapes not just bullet points. We think we want it to be landscape view. Here are some of the parameters:

BHAG:
Become one of the most admired construction companies in the markets we serve within the next 10 years

3 – 5 year goals:
1. Generate 35m in revenue by 2020
2. Have a 50/50 mix of Public-Private job mix
3. Maintain 15% annual growth

1 year goals:
1. $24M in revenue with better margins
2. 14% gross margin on year
3. Business development begins to pay off
4. Continue recruiting great & talented people

Dynamic Quarter Goal:
(Leave this area blank so we can fill it in each quarter please)

Industry/Entity Type

Landscape

Colors
0355a3

Requirements
Must have
• SHAPES OR BOXES FOR VISUAL EFFECT. We don't want it to just be words on a page. Must be creative. Must have our logo somewhere on the poster. Our cmyk blue color is 100-80-0-22. Poster can have different colors, but it just needs to have some of our blue in it.
Should not have
• no bullet points

```html
<!DOCTYPE html>
<html lang="en">
<head>
<meta charset="utf-8">
<title>Halvern Construction – BHAG Poster</title>
<link rel="stylesheet" href="https://fonts.googleapis.com/css2?family=Barlow+Condensed:wght@500;600;700&family=Barlow+Semi+Condensed:wght@500;600&display=swap">
<style>
  :root {
    --brand-blue: #1f3a93;
    --brand-green: #a2c83c;
    --green-dark: #8db32c;
    --ink-navy: #1e2650;
    --body-grey: #2b2b2b;
    --paper: #ffffff;
    --stage: #e9e9e9;
  }
  * { box-sizing: border-box; margin: 0; padding: 0; }
  html, body { width: 1200px; height: 1017px; overflow: hidden; background: var(--stage); }
  .poster {
    position: relative; width: 1200px; height: 1017px;
    background: var(--paper); overflow: hidden;
    font-family: "Barlow Semi Condensed", "Arial Narrow", sans-serif;
  }
  .poster-shapes { position: absolute; inset: 0; }
  .bhag {
    position: absolute; left: 20px; top: 470px; width: 400px;
    text-align: center; color: var(--ink-navy);
    font-family: "Barlow Condensed", sans-serif; font-weight: 500;
    font-size: 42px; line-height: 1.14;
  }
  .bhag .emphasis {
    display: block; color: var(--paper); font-weight: 700;
    font-size: 70px; line-height: 1;
  }
  .company-name {
    position: absolute; left: 50px; top: 908px;
    display: flex; align-items: center; gap: 12px; white-space: nowrap;
    font-family: "Barlow Condensed", sans-serif; font-weight: 700;
    font-size: 40px; letter-spacing: 1px; color: var(--brand-blue);
    text-transform: uppercase;
  }
  .company-name .mark { width: 36px; height: 36px; background: var(--brand-blue); }
  .section-title {
    position: absolute; font-family: "Barlow Condensed", sans-serif;
    font-weight: 700; color: var(--brand-blue); font-size: 50px; letter-spacing: .5px;
    white-space: nowrap; line-height: 1.1;
  }
  .title-long { left: 520px; top: 66px; }
  .title-year { left: 580px; top: 376px; }
  .title-quarter { left: 670px; top: 705px; }
  .goal {
    position: absolute; width: 190px; text-align: center;
    font-size: 19px; line-height: 1.18; color: var(--body-grey); font-weight: 500;
  }
  .goal svg { display: block; margin: 0 auto 10px; }
</style>
</head>
<body>
<main class="poster">
  <svg class="poster-shapes" width="1200" height="1017" viewBox="0 0 1200 1017">
    <defs>
      <linearGradient id="crewTones" x1="0" y1="0" x2="0" y2="1">
        <stop offset="0" stop-color="#9fc1e4"/>
        <stop offset=".45" stop-color="#c9a77a"/>
        <stop offset="1" stop-color="#8c7b66"/>
      </linearGradient>
      <linearGradient id="blueprintTones" x1="0" y1="0" x2="1" y2="1">
        <stop offset="0" stop-color="#7f9fdc"/>
        <stop offset=".6" stop-color="#4d72c4"/>
        <stop offset="1" stop-color="#2f55a8"/>
      </linearGradient>
    </defs>
    <polygon class="bhag-panel" points="0,0 230,0 560,1017 0,1017" fill="var(--brand-green)"/>
    <g role="img" aria-label="Photo of construction workers raising a timber wall frame">
      <polygon points="230,0 520,0 420,400 360,400" fill="url(#crewTones)"/>
    </g>
    <g role="img" aria-label="Photo of rolled blueprints with a yellow folding ruler">
      <polygon points="360,400 420,400 820,1017 560,1017" fill="url(#blueprintTones)"/>
    </g>
  </svg>

  <p class="bhag">Become one<br>of the most<span class="emphasis">admired</span>construction<br>companies in<br>the markets we<br>serve within the<br>next 10 years.</p>

  <div class="company-name"><span class="mark"></span>Halvern Construction</div>

  <h2 class="section-title title-long">3-5 YEAR GOALS:</h2>

  <div class="goal" style="left:490px;top:150px">
    <svg width="90" height="90" viewBox="0 0 90 90"><circle cx="45" cy="45" r="45" fill="var(--brand-green)"/>
      <g fill="var(--brand-blue)" stroke="#fff" stroke-width="2">
        <ellipse cx="45" cy="62" rx="17" ry="6"/><ellipse cx="45" cy="54" rx="17" ry="6"/>
        <ellipse cx="45" cy="46" rx="17" ry="6"/><ellipse cx="45" cy="38" rx="17" ry="6"/><ellipse cx="45" cy="30" rx="17" ry="6"/></g></svg>
    Generate $35m<br>in revenue by 2020
  </div>
  <div class="goal" style="left:690px;top:150px;width:220px">
    <svg width="90" height="90" viewBox="0 0 90 90"><circle cx="45" cy="45" r="45" fill="var(--brand-green)"/>
      <g fill="none" stroke="var(--brand-blue)" stroke-width="7" stroke-linecap="round">
        <path d="M24 42a21 18 0 0 1 36-10"/><path d="M66 48a21 18 0 0 1-36 10"/></g>
      <polygon points="56,22 68,34 54,38" fill="var(--brand-blue)"/><polygon points="34,68 22,56 36,52" fill="var(--brand-blue)"/></svg>
    Have a 50/50 mix of<br>Public-Private job mix
  </div>
  <div class="goal" style="left:930px;top:150px">
    <svg width="90" height="90" viewBox="0 0 90 90">
      <circle cx="45" cy="45" r="40" fill="#d6e8a6"/>
      <path d="M45 45V5A40 40 0 0 1 85 45Z" fill="var(--brand-blue)"/>
      <path d="M45 45H85A40 40 0 0 1 45 85Z" fill="var(--brand-green)"/>
      <path d="M45 45V85A40 40 0 0 1 8 60Z" fill="#bcd979"/></svg>
    Maintain 15%<br>annual growth
  </div>

  <h2 class="section-title title-year">1 YEAR GOALS:</h2>

  <div class="goal" style="left:560px;top:450px;width:170px">
    <svg width="90" height="90" viewBox="0 0 90 90"><circle cx="45" cy="45" r="45" fill="var(--brand-green)"/>
      <g fill="var(--brand-blue)" stroke="#fff" stroke-width="2">
        <ellipse cx="45" cy="62" rx="15" ry="5"/><ellipse cx="45" cy="55" rx="15" ry="5"/><ellipse cx="45" cy="48" rx="15" ry="5"/>
        <ellipse cx="45" cy="41" rx="15" ry="5"/><ellipse cx="45" cy="34" rx="15" ry="5"/></g></svg>
    $24M in<br>revenue with<br>better margins
  </div>
  <div class="goal" style="left:720px;top:430px;width:150px">
    <svg width="110" height="110" viewBox="0 0 110 110">
      <circle cx="60" cy="60" r="42" fill="none" stroke="var(--brand-green)" stroke-width="7"/>
      <path d="M60 60V32M60 60L78 70" stroke="var(--brand-green)" stroke-width="6" stroke-linecap="round"/>
      <circle cx="22" cy="22" r="18" fill="var(--brand-blue)"/>
      <text x="22" y="29" text-anchor="middle" font-family="Barlow Condensed, sans-serif" font-weight="700" font-size="20" fill="#fff">14</text></svg>
    14% gross<br>margin<br>on year
  </div>
  <div class="goal" style="left:865px;top:450px;width:150px">
    <svg width="90" height="90" viewBox="0 0 90 90"><circle cx="45" cy="45" r="45" fill="var(--brand-green)"/>
      <g fill="var(--brand-blue)"><rect x="22" y="42" width="12" height="26" rx="2"/>
        <path d="M37 42l10-18c3-5 9-3 8 3l-3 12h13c4 0 6 3 5 7l-4 16c-1 4-4 6-8 6H37Z"/></g></svg>
    Business<br>development<br>begins to<br>pay off
  </div>
  <div class="goal" style="left:1000px;top:450px;width:150px">
    <svg width="90" height="90" viewBox="0 0 90 90"><circle cx="45" cy="45" r="45" fill="var(--brand-green)"/>
      <g fill="var(--brand-blue)"><circle cx="45" cy="22" r="8"/>
        <path d="M35 33h20v24h-5v18h-10V57h-5Z"/></g></svg>
    Continue<br>recruiting<br>great &amp;<br>talented<br>people
  </div>

  <h2 class="section-title title-quarter">DYNAMIC QUARTER GOAL:</h2>
</main>
</body>
</html>
```